Medical Advertising Website Design
website redesign
Medical Advertising Website Design - Advertising
Creative Brief
Advertising
http://www.kvmedlink.example/
K&V medlink is an ad agency with 100% focus on healthcare (pharmaceutical company) clients. Here is copy for the open web page which gives an overview--
K&V MEDLINK COMMUNICATIONS
YOUR STRATEGIC PARTNER
[GLOBAL HEADLINE]
Raising Strategic Partnership to a Higher Level
TABS
Who We Are
Our Approach
What We Do
Therapeutic Experience
Our Work
Contact Us
At K&V our clients are our partners. We believe that being a great partner means going beyond the expected to bring value through the superior customer experience.
• Strong Key Opinion Leader relationships
• Specialized in “high science” markets
• Industry side experience… “We’ve sat in your chair”
• Superior program financial management
• A leader in managing today’s increased compliance requirements
[Subhead]
Our Mission
“Our customer service mission is to develop superior client relationships built on a mutual trust and a strategic partnership. This partnership is built through our superior industry knowledge, clear understanding of client objectives and expectations, and from the extraordinary value K&V provides beyond the programs we deliver. Our excellence is defined by unwavering quality of work, attention to detail, consistent/timely communications, flexibility to change, and through fair and reasonable pricing. Ultimately, it is our commitment to these values that result in anticipating and exceeding our clients expectations.”
Likes - unique yet professional, clean, crisp design Dislikes - bland, boring appearance. Clutter. Lack of flow. No Flash as iPads / iPhones can't read them.
Service Oriented
PMS 301
bright greens like PMS 362
maybe orange/yellow oranges for emphasis
below header
Company emphasis is strategic partnership for all of their clients

```html
<!DOCTYPE html>
<html lang="en">
<head>
<meta charset="utf-8">
<title>K&amp;V Medlink Communications</title>
<link href="https://fonts.googleapis.com/css2?family=Arimo:wght@400;700&display=swap" rel="stylesheet">
<style>
:root{
  --brand-blue:#005a9c;
  --brand-blue-dark:#004a82;
  --band-blue:#d3e6f2;
  --text-grey:#7d7d7d;
  --sub-grey:#ececec;
  --white:#ffffff;
}
*{margin:0;padding:0;box-sizing:border-box}
html,body{width:1200px;height:923px;overflow:hidden}
body{font-family:"Arimo",Arial,sans-serif;background:var(--white);position:relative;color:var(--text-grey)}
.band{position:absolute;left:0;right:0;top:170px;height:416px;background:var(--band-blue)}
.brand{position:absolute;left:155px;top:35px;display:flex;align-items:center;gap:12px}
.brand-mark{width:58px;height:58px;background:var(--brand-blue)}
.brand-name{font-weight:700;font-size:22px;color:var(--brand-blue);line-height:1.1}
.brand-tag{font-weight:700;font-size:13px;color:var(--brand-blue);letter-spacing:1px;margin-top:4px}
.search{position:absolute;left:848px;top:47px;height:30px;width:167px;display:flex;border:1px solid #c9c9c9}
.search-btn{width:36px;background:var(--brand-blue);display:flex;align-items:center;justify-content:center}
.search-field{flex:1;font-size:11px;color:#9a9a9a;padding:8px 0 0 22px;letter-spacing:.5px}
.panel{position:absolute;left:155px;top:112px;width:898px;height:691px;background:var(--white);box-shadow:0 2px 10px rgba(0,0,0,.35)}
.hero{height:243px;background:linear-gradient(180deg,#eef5fa 0%,#dbe7ef 55%,#bfd3df 100%)}
.nav{height:37px;background:var(--brand-blue);display:flex;position:relative}
.nav a{flex:1;color:var(--white);text-decoration:none;font-size:12px;text-align:center;display:flex;align-items:center;justify-content:center;line-height:1.05;border-right:1px solid rgba(255,255,255,.45)}
.nav a:last-child{border-right:none}
.nav-pointer{position:absolute;left:55px;top:37px;width:0;height:0;border-left:11px solid transparent;border-right:11px solid transparent;border-top:12px solid var(--brand-blue)}
.subbar{height:78px;background:linear-gradient(180deg,#f4f4f4,var(--sub-grey));position:relative}
.home-icon{position:absolute;left:22px;top:28px}
.account{position:absolute;right:40px;top:28px;display:flex;gap:30px}
.account a{display:flex;align-items:center;gap:8px;color:var(--brand-blue);font-size:12px;font-weight:700;text-decoration:none}
.dot{width:24px;height:24px;border-radius:50%;background:var(--brand-blue);display:flex;align-items:center;justify-content:center}
.content{padding:20px 35px 0;font-size:12.5px;text-transform:uppercase;line-height:22.5px}
.intro-list{list-style:none}
.mission-title{color:var(--brand-blue);font-size:18px;font-weight:700;margin-top:28px;line-height:20px}
.mission-text{margin-top:4px;line-height:22px;font-size:12.3px}
.copyright{position:absolute;top:843px;left:0;right:0;text-align:center;color:var(--brand-blue);font-size:12.5px}
.footer{position:absolute;left:155px;top:878px;width:898px;height:45px;background:var(--brand-blue);display:flex;justify-content:center;align-items:center;gap:42px;color:var(--white);font-size:12px}
.footer a{color:var(--white);text-decoration:none}
</style>
</head>
<body>
<div class="band"></div>

<header class="brand">
  <div class="brand-mark"></div>
  <div>
    <div class="brand-name">K&amp;V MEDLINK COMMUNICATIONS</div>
    <div class="brand-tag">YOUR STRATEGIC PARTNER</div>
  </div>
</header>

<div class="search">
  <div class="search-btn">
    <svg width="16" height="16" viewBox="0 0 16 16"><circle cx="9.5" cy="6.5" r="4.5" fill="none" stroke="#fff" stroke-width="2"/><line x1="6" y1="10" x2="2" y2="14" stroke="#fff" stroke-width="2.5"/></svg>
  </div>
  <div class="search-field">SEARCH</div>
</div>

<main class="panel">
  <div class="hero" role="img" aria-label="Group photo of smiling doctors and nurses in white coats and scrubs over a pattern of rounded squares"></div>
  <nav class="nav">
    <a href="#">HOME</a>
    <a href="#">WHO WE ARE</a>
    <a href="#">OUR APPROACH</a>
    <a href="#">WHAT WE DO</a>
    <a href="#">THERAPEUTIC<br>EXPERIENCE</a>
    <a href="#">OUR WORK</a>
    <a href="#">CONTACT US</a>
    <span class="nav-pointer"></span>
  </nav>
  <div class="subbar">
    <svg class="home-icon" width="26" height="22" viewBox="0 0 26 22"><path d="M13 1 L25 11 H21 V21 H16 V14 H10 V21 H5 V11 H1 Z" fill="var(--brand-blue)"/></svg>
    <div class="account">
      <a href="#"><span class="dot"><svg width="6" height="14" viewBox="0 0 6 14"><circle cx="3" cy="2" r="2" fill="#fff"/><rect x="1" y="5" width="4" height="9" fill="#fff"/></svg></span>LOGIN</a>
      <a href="#"><span class="dot"><svg width="12" height="12" viewBox="0 0 12 12"><path d="M1 11 L2 8 L9 1 L11 3 L4 10 Z" fill="#fff"/></svg></span>REGISTER</a>
    </div>
  </div>
  <section class="content">
    <p>A full service medical education agency that goes beyond the expected:</p>
    <ul class="intro-list">
      <li>• Strategically focused</li>
      <li>• Customer service oriented</li>
      <li>• Compliance leadership</li>
    </ul>
    <h2 class="mission-title">OUR MISSION</h2>
    <p class="mission-text">Our customer service mission is to develop superior client relationships built on a mutual trust and a strategic partnership. This partnership is built through our superior industry knowledge, clear understanding of client objectives and expectations, and from the extraordinary value K&amp;V provides beyond the programs we deliver. Our excellence is defined by unwavering quality of work, attention to detail, consistent/timely communications, flexibility to change, and through fair and reasonable pricing. Ultimately, it is our commitment to these values that result in anticipating and exceeding our clients expectations.</p>
  </section>
</main>

<p class="copyright">COPYRIGHT (C) 2012 K&amp;V MEDLINK COMMUNICATIONS</p>

<footer class="footer">
  <a href="#">HOME</a><span>|</span>
  <a href="#">ABOUT</a><span>|</span>
  <a href="#">PRIVACY STATEMENT</a><span>|</span>
  <a href="#">TERMS OF USE</a>
</footer>
</body>
</html>
```